Static landing page for our consulting business

Hi

I require a website for a company called "Quenlo (Pty) Ltd"
It is a management consulting company with three core consulting services.
1. IT
2. Finance
3. Engineering

Our webpage basically needs a landing page with an overview and history of the company.

Then a sub section for each of the three disciplines with a description of what services are rendered. Each of these sections needs to have a link to the consultant that heads up that discipline.

Each consultant of which there are 3 potentially four shortly then needs a page that could introduce themselves, their qualifications etc.

There would also be a 'contact us & information page'
I have attached company logo for your reference.

Target Market(s)

Finance and management consulting

Industry/Entity Type

Business

Coding

Coded - Design and coding required

Number of Pages Required

1 page

Font styles to use
Sans Serif

Colors
33a6d7
85cae6
f68d4d
0492cd
f37122

Requirements
Must have
• basic html page with CSS, no back end or .net. Would run on a php server, and we would add the dynamic content ourselves if required later.
Nice to have
• Social media links, we would code them later.

```html
<!DOCTYPE html>
<html lang="en">
<head>
<meta charset="utf-8">
<title>Quenlo (Pty) Ltd — Consulting</title>
<link rel="stylesheet" href="https://fonts.googleapis.com/css2?family=Open+Sans:wght@400;600;700;800&display=swap">
<style>
  :root {
    --blue: #2a93cf;
    --blue-deep: #0492cd;
    --blue-light: #85cae6;
    --accent: #33a6d7;
    --red: #e8453c;
    --ink: #333333;
    --muted: #8a8a8a;
    --line: #e3e3e3;
    --bg-soft: #f4f4f4;
    --white: #ffffff;
  }
  * { box-sizing: border-box; margin: 0; padding: 0; }
  html, body { width: 1200px; height: 2528px; overflow: hidden; }
  body { font-family: "Open Sans", Arial, sans-serif; color: var(--ink); background: var(--white); }

  /* Header */
  .site-header { height: 100px; display: flex; align-items: center; justify-content: space-between; padding: 0 100px; background: var(--white); }
  .brand { display: flex; align-items: center; gap: 10px; font-weight: 800; font-size: 26px; color: #1f2f4a; }
  .brand-dot { width: 14px; height: 14px; border-radius: 50%; background: var(--blue); }
  .main-nav { display: flex; align-items: center; gap: 28px; font-size: 13px; }
  .main-nav a { color: #555; text-decoration: none; }
  .main-nav a.active { color: var(--blue); font-weight: 600; }
  .social { display: flex; gap: 8px; padding-left: 14px; border-left: 1px solid var(--line); }
  .social span { width: 10px; height: 10px; border-radius: 50%; background: #9a9a9a; }

  /* Hero */
  .hero { position: relative; height: 520px; }
  .hero-photo { position: absolute; inset: 0; background: linear-gradient(100deg, #d9dde2 0%, #eef0f2 40%, #c9ced6 70%, #e7e9ec 100%); }
  .hero-caption { position: absolute; left: 100px; top: 440px; background: var(--blue); color: var(--white); font-weight: 700; font-size: 28px; padding: 14px 40px 14px 24px; }
  .hero-arrow { position: absolute; top: 240px; width: 34px; height: 34px; border-radius: 50%; background: rgba(60,60,60,.55); display: flex; align-items: center; justify-content: center; }
  .hero-arrow.prev { left: 12px; } .hero-arrow.next { right: 12px; }

  /* Section headings */
  .section-title { text-align: center; font-weight: 800; font-size: 36px; letter-spacing: 2px; color: #2b2b2b; }
  .section-sub { text-align: center; color: var(--accent); font-size: 17px; letter-spacing: 1px; margin-top: 4px; }

  /* Services */
  .services { height: 610px; background: var(--bg-soft); padding-top: 110px; }
  .service-cards { display: flex; margin: 60px 100px 0; background: var(--white); box-shadow: 0 10px 24px rgba(0,0,0,.08); }
  .service-card { flex: 1; height: 300px; padding: 80px 50px 0; text-align: center; border-top: 4px solid transparent; border-right: 1px solid var(--line); }
  .service-card:last-child { border-right: none; }
  .service-card.featured { border-top-color: var(--blue); }
  .service-card h3 { font-size: 16px; font-weight: 700; margin: 18px 0 12px; letter-spacing: 1px; }
  .service-card p { font-size: 12px; color: var(--muted); line-height: 1.6; }

  /* About */
  .about { position: relative; height: 530px; background: var(--blue); color: var(--white); padding: 130px 0 0 100px; }
  .about h2 { font-size: 36px; font-weight: 800; letter-spacing: 2px; }
  .about h4 { font-size: 15px; font-weight: 700; letter-spacing: 1px; line-height: 1.6; margin-top: 18px; width: 420px; }
  .about p { font-size: 13px; line-height: 1.7; width: 520px; margin-top: 36px; opacity: .95; }
  .btn-more { display: inline-block; margin-top: 40px; background: var(--red); color: var(--white); font-size: 12px; font-weight: 700; padding: 9px 18px; }
  .about-media { position: absolute; left: 700px; top: 90px; width: 360px; height: 460px; border-radius: 18px; background: linear-gradient(160deg, #f2e3d6 0%, #d9dce4 55%, #c6ccd8 100%); }

  /* Contact */
  .contact { height: 670px; background: var(--bg-soft); padding-top: 120px; }
  .contact-card { display: flex; gap: 60px; margin: 50px 100px 0; height: 360px; background: var(--white); padding: 40px 40px; box-shadow: 0 10px 24px rgba(0,0,0,.08); }
  .contact-info { width: 220px; font-size: 12px; color: var(--muted); line-height: 1.6; }
  .contact-info h5 { color: var(--ink); font-size: 13px; font-weight: 700; margin-bottom: 18px; }
  .contact-info p { margin-bottom: 26px; }
  .contact-info a { display: block; color: var(--blue); text-decoration: underline; }
  .contact-form { flex: 1; display: flex; flex-direction: column; gap: 16px; }
  .form-row { display: flex; gap: 20px; }
  .field { flex: 1; height: 40px; border: 1px solid var(--line); }
  .field.message { height: 150px; flex: none; }
  .btn-submit { align-self: flex-start; font-size: 12px; font-weight: 700; padding: 8px 2px; }

  /* Footer */
  .site-footer { height: 98px; background: var(--blue); color: var(--white); display: flex; align-items: center; justify-content: center; font-size: 12px; }
</style>
</head>
<body>
  <header class="site-header">
    <div class="brand"><span class="brand-dot"></span>Quenlo (Pty) Ltd</div>
    <nav class="main-nav">
      <a class="active" href="#">Home</a>
      <a href="#">About Us</a>
      <a href="#">Services</a>
      <a href="#">Gallery</a>
      <a href="#">Testimonials</a>
      <a href="#">Contact Us</a>
      <div class="social"><span></span><span></span><span></span><span></span></div>
    </nav>
  </header>

  <section class="hero">
    <div class="hero-photo" role="img" aria-label="Photo of consultants meeting around a table in a bright office"></div>
    <div class="hero-caption">We are a consulting company</div>
    <div class="hero-arrow prev"><svg width="12" height="12" viewBox="0 0 12 12"><path d="M8 1 3 6l5 5" fill="none" stroke="#fff" stroke-width="2"/></svg></div>
    <div class="hero-arrow next"><svg width="12" height="12" viewBox="0 0 12 12"><path d="M4 1l5 5-5 5" fill="none" stroke="#fff" stroke-width="2"/></svg></div>
  </section>

  <section class="services">
    <h2 class="section-title">WELCOME TO OUR SITE</h2>
    <div class="section-sub">OUR BUSINESS VERTICALS</div>
    <div class="service-cards">
      <div class="service-card">
        <svg width="30" height="30" viewBox="0 0 30 30"><circle cx="15" cy="15" r="12" fill="var(--blue)"/><path d="M3 15h24M15 3c-6 7-6 17 0 24M15 3c6 7 6 17 0 24" fill="none" stroke="#fff" stroke-width="1.5"/></svg>
        <h3>IT</h3>
        <p>Servicing your systems, networks and software with clear and steady support.</p>
      </div>
      <div class="service-card featured">
        <svg width="34" height="30" viewBox="0 0 34 30"><rect x="2" y="6" width="30" height="18" rx="2" fill="var(--blue)"/><circle cx="17" cy="15" r="5" fill="none" stroke="#fff" stroke-width="1.5"/></svg>
        <h3>FINANCING</h3>
        <p>Sound financial planning, budgeting and reporting for growing teams today.</p>
      </div>
      <div class="service-card">
        <svg width="34" height="30" viewBox="0 0 34 30"><circle cx="12" cy="17" r="8" fill="none" stroke="var(--blue)" stroke-width="4" stroke-dasharray="3 2"/><circle cx="12" cy="17" r="3" fill="var(--blue)"/><circle cx="25" cy="8" r="5" fill="none" stroke="var(--blue)" stroke-width="3" stroke-dasharray="2 2"/></svg>
        <h3>ENGINEERING</h3>
        <p>Practical engineering advice from design review to final project delivery.</p>
      </div>
    </div>
  </section>

  <section class="about">
    <h2>ABOUT US</h2>
    <h4>DONEC ODIO QUISQUE VOLUTPAT MATTIS EROS NULLAM</h4>
    <p>We guide organisations through change with practical advice in technology, finance and engineering. Our consultants work beside your teams to find clear answers, plan sensible steps and deliver results that last. Founded on trust and experience, we keep every engagement focused and simple.</p>
    <span class="btn-more">READ MORE</span>
    <div class="about-media" role="img" aria-label="Hands holding a tablet showing a portrait of a smiling consultant"></div>
  </section>

  <section class="contact">
    <h2 class="section-title">CONTACT US</h2>
    <div class="section-sub">FOR MORE INFO</div>
    <div class="contact-card">
      <div class="contact-info">
        <h5>ADDRESS</h5>
        <p>Suite 4, Harbour Park, 12 Main Road, Cape Town</p>
        <p>Open Monday to Friday, 8am to 5pm. Visits by appointment.</p>
        <a href="#">info@quenlo.com</a>
        <a href="#">sales@quenlo.com</a>
        <a href="#">support@quenlo.com</a>
      </div>
      <form class="contact-form">
        <div class="form-row"><div class="field"></div><div class="field"></div></div>
        <div class="field message"></div>
        <span class="btn-submit">SUBMIT</span>
      </form>
    </div>
  </section>

  <footer class="site-footer">Copyright © Website 2014. All Rights Reserved</footer>
</body>
</html>
```